Antigen Preservation Bureau

The company will provide a contract research services to stabilize various viruses, viral vectors, and vaccines. It may offer some licensing opportunities for stabilizing technologies. Main area of applications are pharmaceutical, therapeutic, and vaccination field. The company aspires to develop room temperature vaccines for global distribution beyond the current cold chain.

Target Market(s)

pharmaceutical, therapeutic and vaccination fields

Coding

Coded - Design and coding required

Number of Pages Required

4 page

Requirements
Must have
• Incorporate a APB logo, attached at the bottom, on the Web page

```html
<!DOCTYPE html>
<html lang="en">
<head>
<meta charset="utf-8">
<title>Antigen Preservation Bureau</title>
<link href="https://fonts.googleapis.com/css2?family=Poppins:wght@300;400;500;600;700&display=swap" rel="stylesheet">
<style>
:root{
  --green:#5ba688;
  --green-dark:#4c9176;
  --gold:#d6a24c;
  --ink:#333333;
  --muted:#555555;
  --soft:#f3f3f3;
  --footer:#8b8b8b;
  --white:#ffffff;
}
*{box-sizing:border-box;margin:0;padding:0}
html,body{width:1200px;height:3175px;overflow:hidden}
body{font-family:"Poppins",Arial,sans-serif;color:var(--ink);background:var(--white);position:relative}
.abs{position:absolute}

/* header */
.site-header{position:absolute;left:0;top:0;width:1200px;height:89px;background:var(--white);border-top:4px solid var(--gold)}
.brand{position:absolute;left:138px;top:22px;display:flex;align-items:center;gap:14px}
.brand-mark{width:40px;height:40px;border:3px solid var(--green)}
.brand-name{font-size:17px;font-weight:500;color:var(--green);letter-spacing:2px;line-height:19px;width:220px;text-transform:uppercase}
.contact-tab{position:absolute;left:760px;top:0;width:320px;height:34px;background:var(--gold);border-radius:0 0 0 18px;display:flex;align-items:center;justify-content:center;gap:26px;color:var(--white);font-size:14px}
.contact-tab span{display:flex;align-items:center;gap:7px}
.main-nav{position:absolute;left:566px;top:56px;display:flex;gap:0;font-size:14px}
.main-nav a{color:var(--ink);text-decoration:none;margin-right:48px}
.main-nav a.active{color:var(--green)}
.main-nav a.news{font-size:16px}

/* hero */
.hero{position:absolute;left:0;top:89px;width:1200px;height:538px;background:linear-gradient(110deg,#5b6f80 0%,#c9d3dc 35%,#e9edf1 60%,#b9c2c8 100%)}
.hero-arrow{position:absolute;top:258px;width:26px;height:26px;background:#2d2d2d;display:flex;align-items:center;justify-content:center}
.hero-title{position:absolute;left:0;width:1200px;top:460px;text-align:center;color:var(--white);font-size:26px;font-weight:700;line-height:36px;text-shadow:0 2px 6px rgba(0,0,0,.55)}

/* section headings */
.section-title{position:absolute;left:0;width:1200px;text-align:center;font-size:22px;font-weight:400;color:var(--green)}
.section-title .plain{color:var(--muted)}
.section-title::after{content:"";display:block;width:120px;height:2px;background:var(--green);margin:10px auto 0}
.section-lead{position:absolute;left:200px;width:800px;text-align:center;font-size:12.5px;line-height:24px;color:var(--muted)}

/* feature cards */
.feature-card{position:absolute;width:286px;background:var(--soft);box-shadow:0 2px 10px rgba(0,0,0,.2);border:6px solid var(--white);text-align:center;padding-top:28px}
.feature-card.active{background:var(--green);color:var(--white)}
.feature-card h3{font-size:16px;font-weight:500;color:var(--gold);margin-top:14px}
.feature-card.active h3{color:var(--white)}
.feature-card p{font-size:12.5px;line-height:22px;color:var(--ink);margin:4px 22px 0}
.feature-card.active p{color:var(--white)}

/* about */
.about{position:absolute;left:0;top:1065px;width:1200px;height:427px;background:var(--soft)}
.about-title{position:absolute;left:138px;top:60px;font-size:21px;color:var(--green)}
.about-title .plain{color:var(--muted)}
.about-title::after{content:"";display:block;width:120px;height:2px;background:var(--green);margin-top:6px}
.about-text{position:absolute;left:138px;top:106px;width:440px;font-size:12.5px;line-height:23px;color:var(--ink)}
.about-text p+p{margin-top:8px}
.btn{display:inline-block;background:var(--gold);color:var(--white);font-size:12px;font-weight:500;border-radius:16px;padding:6px 18px}
.video-box{position:absolute;left:612px;top:97px;width:446px;height:246px;background:#3d3d3d;color:var(--white)}
.video-label{position:absolute;left:50px;top:86px;font-size:32px;font-weight:300;line-height:34px}
.video-label .l2{display:block;padding-left:190px}
.video-rule{position:absolute;left:50px;top:125px;width:170px;height:2px;background:var(--white)}
.video-play{position:absolute;left:198px;top:100px;width:50px;height:36px;border-radius:8px;background:#d42a2a;display:flex;align-items:center;justify-content:center}

/* news */
.news-card{position:absolute;top:1605px;width:282px;height:434px;border:1px solid #e3e3e3;background:var(--white);text-align:center}
.news-photo{height:213px}
.news-date{position:absolute;left:0;top:0;width:50px;text-align:center;color:var(--white)}
.news-date .day{display:block;background:var(--green);font-size:24px;line-height:32px}
.news-date .mon{display:block;background:var(--gold);font-size:9px;line-height:14px}
.news-card h3{font-size:14px;font-weight:400;color:var(--green);line-height:22px;margin:14px 26px 0}
.news-card p{font-size:12px;line-height:22px;color:var(--ink);margin:14px 22px 0}
.news-card .more{display:block;font-size:12px;font-style:italic;color:var(--gold);margin-top:14px}

/* applications */
.applications{position:absolute;left:0;top:2089px;width:1200px;height:464px;background:var(--soft)}

/* licensing */
.licensing{position:absolute;left:155px;top:2608px;width:885px;height:233px;background:var(--white);border-radius:14px;box-shadow:0 4px 14px rgba(0,0,0,.25);text-align:center;z-index:2}
.licensing h2{font-size:21px;font-weight:400;color:var(--ink);margin-top:42px}
.licensing p{font-size:12.5px;line-height:24px;color:var(--muted);margin:10px 80px 0}
.licensing .call{display:inline-flex;align-items:center;gap:8px;background:var(--gold);color:var(--white);font-size:14px;padding:6px 16px;margin-top:12px;border-radius:2px}

/* footer */
.site-footer{position:absolute;left:0;top:2799px;width:1200px;height:330px;background:var(--footer);color:var(--white)}
.footer-col{position:absolute;top:110px;font-size:12.5px}
.footer-col h4{font-size:13px;font-weight:400}
.footer-col h4::after{content:"";display:block;width:40px;height:2px;background:var(--white);margin-top:8px}
.quick-links li{list-style:none;line-height:25px}
.contact-line{display:flex;gap:14px;margin-top:16px;line-height:17px}
.map{width:226px;height:146px;background:linear-gradient(135deg,#e9ecef,#d5dde2);margin-top:14px}
.social{display:flex;gap:10px;margin-top:16px}
.social i{display:block;width:22px;height:22px;border-radius:50%}
.footer-brand{display:flex;align-items:center;gap:12px;margin-top:16px}
.footer-brand .sq{width:34px;height:34px;border:3px solid var(--white)}
.footer-brand span{font-size:14px;letter-spacing:2px;line-height:16px;text-transform:uppercase;width:160px}
.bottom-bar{position:absolute;left:0;top:3129px;width:1200px;height:46px;background:var(--gold);color:var(--white);font-size:11px}
.bottom-bar .copy{position:absolute;left:138px;top:17px}
.bottom-bar .legal{position:absolute;right:142px;top:17px}
</style>
</head>
<body>

<header class="site-header">
  <div class="brand"><div class="brand-mark"></div><div class="brand-name">Antigen Preservation Bureau</div></div>
  <div class="contact-tab">
    <span><svg width="16" height="16" viewBox="0 0 24 24"><circle cx="12" cy="12" r="11" fill="none" stroke="#fff" stroke-width="2"/><path d="M8 6l2 3-1.5 1.5a8 8 0 0 0 5 5L15 14l3 2-1 2.5c-6 0-11-5-11-11z" fill="#fff"/></svg>123.456.7890</span>
    <span><svg width="20" height="14" viewBox="0 0 20 14"><rect x="1" y="1" width="18" height="12" fill="none" stroke="#fff" stroke-width="1.6"/><path d="M1 1l9 7 9-7" fill="none" stroke="#fff" stroke-width="1.6"/></svg>inquiry@apb.com</span>
  </div>
  <nav class="main-nav">
    <a class="active">Home</a><a>About Us</a><a>Services</a><a class="news">News</a><a>Contact Us</a>
  </nav>
</header>

<section class="hero" role="img" aria-label="Two scientists in lab coats and safety glasses examining a flask in a laboratory">
  <div class="hero-arrow" style="left:0"><svg width="10" height="12"><path d="M8 1L2 6l6 5" fill="none" stroke="#fff" stroke-width="2"/></svg></div>
  <div class="hero-arrow" style="right:0"><svg width="10" height="12"><path d="M2 1l6 5-6 5" fill="none" stroke="#fff" stroke-width="2"/></svg></div>
  <h1 class="hero-title">We Provide A Contract Research Services To Stabilize Various Viruses,<br>Viral Vectors, And Vaccines.</h1>
</section>

<h2 class="section-title" style="top:676px">Providing A Contract Research <span class="plain">Services To</span></h2>
<p class="section-lead" style="top:720px">Lorem ipsum dolor sit amet, consectetuer adipiscing elit, sed diam nonummy nibh euismod tincidunt ut laoreet dolore magna aliquam erat volutpat. Ut wisi enim ad minim veniam, quis nostrud exerci tation ullamcorper.</p>

<div class="feature-card" style="left:136px;top:790px;height:247px">
  <svg width="70" height="70" viewBox="0 0 70 70"><g stroke="#d6a24c" stroke-width="3"><line x1="35" y1="8" x2="35" y2="62"/><line x1="8" y1="35" x2="62" y2="35"/><line x1="16" y1="16" x2="54" y2="54"/><line x1="54" y1="16" x2="16" y2="54"/></g><circle cx="35" cy="35" r="16" fill="#d6a24c"/><g fill="#d6a24c"><circle cx="35" cy="8" r="4"/><circle cx="35" cy="62" r="4"/><circle cx="8" cy="35" r="4"/><circle cx="62" cy="35" r="4"/><circle cx="16" cy="16" r="4"/><circle cx="54" cy="54" r="4"/><circle cx="54" cy="16" r="4"/><circle cx="16" cy="54" r="4"/></g></svg>
  <h3>Stabilize Various Viruses</h3>
  <p>Lorem ipsum dolor sit amet, consectetuer adipiscing elit, sed diam non...</p>
</div>
<div class="feature-card active" style="left:450px;top:790px;height:247px">
  <svg width="90" height="70" viewBox="0 0 90 70"><g stroke="#fff" stroke-width="2" fill="none"><line x1="45" y1="10" x2="45" y2="35"/><line x1="45" y1="35" x2="20" y2="30"/><line x1="45" y1="35" x2="70" y2="30"/><line x1="45" y1="35" x2="28" y2="55"/><line x1="45" y1="35" x2="62" y2="55"/><line x1="20" y1="30" x2="6" y2="40"/><line x1="70" y1="30" x2="84" y2="40"/></g><g fill="#fff"><circle cx="45" cy="10" r="5"/><circle cx="45" cy="35" r="6"/><circle cx="20" cy="30" r="4"/><circle cx="70" cy="30" r="4"/><circle cx="28" cy="55" r="4"/><circle cx="62" cy="55" r="4"/><circle cx="6" cy="40" r="3"/><circle cx="84" cy="40" r="3"/></g></svg>
  <h3>Viral Vectors</h3>
  <p>Lorem ipsum dolor sit amet, consectetuer adipiscing elit, sed diam non...</p>
</div>
<div class="feature-card" style="left:762px;top:790px;height:247px">
  <svg width="70" height="70" viewBox="0 0 70 70"><g stroke="#d6a24c" stroke-width="3" fill="none" stroke-linecap="round"><line x1="8" y1="62" x2="20" y2="50"/><rect x="22" y="24" width="14" height="34" transform="rotate(45 29 41)"/><line x1="44" y1="20" x2="54" y2="30"/><line x1="49" y1="25" x2="58" y2="16"/><line x1="54" y1="12" x2="62" y2="20"/></g></svg>
  <h3>Vaccines</h3>
  <p>Lorem ipsum dolor sit amet, consectetuer adipiscing elit, sed diam non...</p>
</div>

<section class="about">
  <h2 class="about-title">About Antigen Preservation <span class="plain">Bureau</span></h2>
  <div class="about-text">
    <p>Lorem ipsum dolor sit amet, consectetuer adipiscing elit, sed diam nonummy nibh euismod tincidunt ut laoreet dolore maa aliquam erat volutpat. Ut wisi enim ad minim veniam, quis nostrud exerci tation ullamcorper suscipit lobortis nisl ut aliquip ex ea.</p>
    <p>Lit, sed diam nonummy nibh euismod tincidunt ut laoreet dolore mana aliquam erat volutpat. Ut wisi enim ad minim veniam, quis nostrud exerci tation ullamcorper suscipit. nonummy nibh euismod tincidunt ut laoreet.</p>
    <p style="margin-top:16px"><span class="btn">Read More</span></p>
  </div>
  <div class="video-box">
    <div class="video-label">Antigen Preservation<span class="l2">Bureau</span></div>
    <div class="video-rule"></div>
    <div class="video-play"><svg width="14" height="16"><path d="M1 1l12 7-12 7z" fill="#fff"/></svg></div>
  </div>
</section>

<h2 class="section-title" style="top:1546px">Latest <span class="plain">News</span></h2>

<article class="news-card" style="left:138px">
  <div class="news-photo" role="img" aria-label="Gloved hand holding a petri dish in a laboratory" style="background:linear-gradient(135deg,#2f6f9a,#9fc6df)"></div>
  <div class="news-date"><span class="day">05</span><span class="mon">JAN '19</span></div>
  <h3>Lit, sed diam nonummy niby nib euismod tincidunt ut laoreet.</h3>
  <p>Lorem ipsum dolor sit amet nsectetuer adipiscing elit, sed diam nonummy nibh euismod tincidunt ut laoreet dolore maa aliquam erat volutpat.</p>
  <span class="more">Continue Reading →</span>
</article>
<article class="news-card" style="left:455px">
  <div class="news-photo" role="img" aria-label="Medicine vial with a blue cap lying on its side" style="background:linear-gradient(135deg,#f2f2f2,#b8bcc0)"></div>
  <div class="news-date"><span class="day">05</span><span class="mon">JAN '19</span></div>
  <h3>Lit, sed diam nonummy niby nib euismod tincidunt ut laoreet.</h3>
  <p>Lorem ipsum dolor sit amet nsectetuer adipiscing elit, sed diam nonummy nibh euismod tincidunt ut laoreet dolore maa aliquam erat volutpat.</p>
  <span class="more">Continue Reading →</span>
</article>
<article class="news-card" style="left:773px">
  <div class="news-photo" role="img" aria-label="Researcher operating laboratory equipment with sample bags" style="background:linear-gradient(135deg,#6b6f72,#d8dadb)"></div>
  <div class="news-date"><span class="day">05</span><span class="mon">JAN '19</span></div>
  <h3>Lit, sed diam nonummy niby nib euismod tincidunt ut laoreet.</h3>
  <p>Lorem ipsum dolor sit amet nsectetuer adipiscing elit, sed diam nonummy nibh euismod tincidunt ut laoreet dolore maa aliquam erat volutpat.</p>
  <span class="more">Continue Reading →</span>
</article>

<section class="applications">
  <h2 class="section-title" style="top:62px">Our Main Area <span class="plain">of Applications Are</span></h2>
  <p class="section-lead" style="top:106px">Lorem ipsum dolor sit amet, consectetuer adipiscing elit, sed diam nonummy nibh euismod tincidunt ut laoreet dolore magna aliquam erat volutpat. Ut wisi enim ad minim veniam, quis nostrud exerci tation ullamcorper.</p>
  <div class="feature-card" style="left:138px;top:172px;height:218px;padding-top:22px">
    <svg width="64" height="70" viewBox="0 0 64 70"><rect x="6" y="6" width="22" height="50" rx="11" transform="rotate(-25 17 31)" fill="#d6a24c"/><rect x="34" y="22" width="22" height="44" rx="11" transform="rotate(-50 45 44)" fill="#d6a24c"/><line x1="8" y1="30" x2="28" y2="22" stroke="#fff" stroke-width="3"/></svg>
    <h3>Pharmaceutical</h3>
    <p>Lorem ipsum dolor sit amet, consectetuer adipiscing elit, sed diam non...</p>
  </div>
  <div class="feature-card active" style="left:454px;top:172px;height:218px;padding-top:22px">
    <svg width="80" height="70" viewBox="0 0 80 70"><path d="M40 36C28 26 24 22 24 16a8 8 0 0 1 16-2 8 8 0 0 1 16 2c0 6-4 10-16 20z" fill="#fff"/><path d="M6 30v18l14 16h14V52L22 40M74 30v18L60 64H46V52l12-12" fill="none" stroke="#fff" stroke-width="3"/></svg>
    <h3>Therapeutic</h3>
    <p>Lorem ipsum dolor sit amet, consectetuer adipiscing elit, sed diam non...</p>
  </div>
  <div class="feature-card" style="left:766px;top:172px;height:218px;padding-top:22px">
    <svg width="70" height="70" viewBox="0 0 70 70"><g stroke="#d6a24c" stroke-width="3" fill="none" stroke-linecap="round"><line x1="8" y1="62" x2="20" y2="50"/><rect x="22" y="24" width="14" height="34" transform="rotate(45 29 41)"/><line x1="44" y1="20" x2="54" y2="30"/><line x1="49" y1="25" x2="58" y2="16"/><line x1="54" y1="12" x2="62" y2="20"/></g></svg>
    <h3>Vaccination</h3>
    <p>Lorem ipsum dolor sit amet, consectetuer adipiscing elit, sed diam non...</p>
  </div>
</section>

<section class="licensing">
  <h2>Also offering some licensing opportunities for stabilizing technologies.</h2>
  <p>Lorem ipsum dolor sit amet, consectetuer adipiscing elit, sed diam nonummy nibh euismod tincidunt ut laoreet dolore magna aliquam erat volutpat. Ut wisi enim ad minim veniam, quis nostrud exerci tation ullamcorper.</p>
  <span class="call"><svg width="16" height="16" viewBox="0 0 24 24"><circle cx="12" cy="12" r="11" fill="none" stroke="#fff" stroke-width="2"/><path d="M8 6l2 3-1.5 1.5a8 8 0 0 0 5 5L15 14l3 2-1 2.5c-6 0-11-5-11-11z" fill="#fff"/></svg>123.456.7890</span>
</section>

<footer class="site-footer">
  <div class="footer-col" style="left:140px">
    <h4>Quick Links</h4>
    <ul class="quick-links" style="margin-top:12px"><li>Home</li><li>About Us</li><li>Services</li><li>News</li><li>Contact Us</li></ul>
  </div>
  <div class="footer-col" style="left:290px">
    <h4>Contact Details</h4>
    <div class="contact-line"><svg width="14" height="18" viewBox="0 0 14 18"><path d="M7 0a7 7 0 0 1 7 7c0 5-7 11-7 11S0 12 0 7a7 7 0 0 1 7-7z" fill="#fff"/><circle cx="7" cy="7" r="2.5" fill="#8b8b8b"/></svg><span>Antigen Preservation Bureau<br>Street Name, City<br>Name State Zipcode</span></div>
    <div class="contact-line" style="margin-top:22px"><svg width="14" height="14" viewBox="0 0 24 24"><circle cx="12" cy="12" r="11" fill="none" stroke="#fff" stroke-width="2"/><path d="M8 6l2 3-1.5 1.5a8 8 0 0 0 5 5L15 14l3 2-1 2.5c-6 0-11-5-11-11z" fill="#fff"/></svg><span>123.456.7890</span></div>
    <div class="contact-line" style="margin-top:22px"><svg width="16" height="12" viewBox="0 0 20 14"><rect x="1" y="1" width="18" height="12" fill="none" stroke="#fff" stroke-width="1.6"/><path d="M1 1l9 7 9-7" fill="none" stroke="#fff" stroke-width="1.6"/></svg><span>inquiry@apb.com</span></div>
  </div>
  <div class="footer-col" style="left:535px">
    <h4>Location Map</h4>
    <div class="map" role="img" aria-label="Street map showing the office location"></div>
  </div>
  <div class="footer-col" style="left:804px">
    <h4>Follow Us On</h4>
    <div class="social"><i style="background:#e0a43d"></i><i style="background:#5ba688"></i><i style="background:#5ba688"></i></div>
    <div class="footer-brand"><div class="sq"></div><span>Antigen Preservation Bureau</span></div>
  </div>
</footer>

<div class="bottom-bar">
  <span class="copy">Copyright © 2019 Antigen Preservation Bureau. All Rights Reserved.</span>
  <span class="legal">Terms &amp; Conditions | Privacy Policy</span>
</div>

</body>
</html>
```